I have a small construction company that is growing. I specialize in commercial concrete and custom

I want a site that shows what we do. We specialize in custom deck design and builds. Custom home builds. Commercial concrete . project management

Target Market(s)

Commercial construction companies and custom home builders

Industry/Entity Type

Construction

Number of Pages Required

1 page

Font styles to use
Serif

Colors

Designer to choose colors to be used in the design.

Requirements
Must have
• Pictures and videos of project that we have completed or are in progress

```html
<!DOCTYPE html>
<html lang="en">
<head>
<meta charset="utf-8">
<title>Construction Company</title>
<link href="https://fonts.googleapis.com/css2?family=Lato:wght@300;400;700;900&family=Oswald:wght@400;500&display=swap" rel="stylesheet">
<style>
:root{
  --yellow:#f9c20f;
  --black:#111111;
  --deep:#0b0b0b;
  --text:#555555;
  --muted:#9a9a9a;
  --white:#ffffff;
  --line:#f3cf55;
}
*{box-sizing:border-box;margin:0;padding:0}
html,body{width:1200px;height:4569px;overflow:hidden}
body{position:relative;background:var(--white);font-family:'Lato',sans-serif;color:var(--text)}
.abs{position:absolute}
.photo{position:absolute}
.btn{position:absolute;background:var(--yellow);color:var(--black);border-radius:18px;font-size:14px;font-weight:700;text-align:center;line-height:32px;width:130px;height:32px}
.rule{position:absolute;left:122px;width:958px;height:2px;background:var(--line)}
.section-title{position:absolute;left:0;width:1200px;text-align:center;font-size:28px;font-weight:400;color:var(--black);letter-spacing:.5px}
.section-title b{font-weight:900;position:relative;display:inline-block;padding:14px 10px 6px 4px;margin-left:2px}
.section-title b::after{content:"";position:absolute;left:-6px;top:0;right:-14px;bottom:-8px;border:3px solid var(--yellow);border-left:none}
.section-title b::before{content:"";position:absolute;left:-6px;top:0;width:3px;height:20px;background:var(--yellow)}
.section-title b.plain{font-weight:400;padding:14px 10px 6px 0;margin-left:0}
.arrows{position:absolute;display:flex;gap:8px}
/* nav */
.nav{position:absolute;left:0;top:0;width:1200px;height:76px;background:var(--black)}
.logo{position:absolute;left:100px;top:0;width:265px;height:76px;background:var(--yellow);font-size:36px;font-weight:700;color:var(--black);line-height:76px;padding-left:22px}
.nav ul{position:absolute;left:345px;top:0;list-style:none;display:flex;height:76px;align-items:center}
.nav li{color:var(--white);font-size:13px;font-weight:700;margin-left:20px;white-space:nowrap}
.nav li.active{position:relative}
.nav li.active::before{content:"";position:absolute;left:50%;top:-30px;margin-left:-14px;border:14px solid transparent;border-top-color:var(--white);border-bottom:none}
.quote{position:absolute;left:978px;top:26px;width:102px;height:24px;background:var(--yellow);border-radius:12px;color:var(--black);font-size:11px;font-weight:700;text-align:center;line-height:24px}
/* hero */
.hero-text{position:absolute;left:0;width:1200px;text-align:center}
/* stats */
.stats{position:absolute;left:0;top:630px;width:1200px;height:138px;background:var(--black)}
/* services */
.spec-title{position:absolute;left:603px;top:958px;font-size:27px;font-weight:700;color:var(--black)}
.spec-copy{position:absolute;left:603px;top:1002px;font-size:14px;color:var(--text)}
.service{position:absolute;top:1090px;width:190px;text-align:center;font-size:12px;color:var(--black);white-space:nowrap}
.service svg{display:block;margin:0 auto 10px}
/* projects */
.proj-hover{position:absolute;left:600px;top:1435px;width:300px;height:243px;background:rgba(249,194,15,.92)}
/* about */
.about-copy{position:absolute;left:122px;top:1995px;width:480px;font-size:14px;line-height:17px;color:var(--text)}
/* testimonials */
.t-card{position:absolute;background:var(--black);color:var(--white);text-align:center}
.t-card.featured{background:var(--yellow);color:var(--black)}
.t-card .mark{position:absolute;left:16px;top:12px;font-family:'Oswald',sans-serif;font-size:60px;line-height:60px;font-weight:500}
.t-card .name{font-family:'Oswald',sans-serif;font-size:18px}
.t-card .role{font-size:12px}
.t-card .stars{color:var(--yellow);font-size:14px;letter-spacing:2px;margin:4px 0 8px}
.t-card.featured .stars{color:var(--black)}
.t-card p{font-size:13px;line-height:17px;padding:0 26px}
.t-card .more{font-size:12px;margin-top:16px}
.avatar{position:absolute;border-radius:50%;border:4px solid var(--yellow);background:linear-gradient(160deg,#c9b39a,#6c5646)}
.dots{position:absolute;display:flex;gap:12px}
.dots span{width:14px;height:14px;border-radius:50%;background:var(--black)}
.dots span.on{background:var(--yellow);border:2px solid var(--black)}
/* blog */
.blog{position:absolute;top:2961px;height:420px;background:var(--black);color:var(--white);text-align:center}
.blog.featured{background:var(--yellow);color:var(--black)}
.blog .img{position:absolute;left:0;top:0;width:100%;height:207px}
.date{position:absolute;left:50%;top:170px;margin-left:-42px;width:84px;height:84px;border-radius:50%;background:var(--white);border:4px solid var(--yellow);color:var(--black);text-align:center;font-size:10px;padding-top:10px}
.date b{display:block;font-family:'Oswald',sans-serif;font-size:30px;line-height:34px;font-weight:400}
.blog h3{position:absolute;top:268px;width:100%;font-family:'Oswald',sans-serif;font-weight:400;font-size:30px}
.blog p{position:absolute;top:320px;width:100%;padding:0 30px;font-size:13px;line-height:17px}
.blog .meta{position:absolute;left:20px;right:20px;top:386px;font-size:11px;display:flex;justify-content:space-between}
/* subscribe */
.subscribe-box{position:absolute;left:359px;top:3724px;width:485px;height:44px;border:2px solid #777;border-radius:22px;overflow:hidden}
.subscribe-box span{position:absolute;left:24px;top:12px;font-size:11px;color:var(--text)}
.subscribe-box i{position:absolute;right:0;top:0;width:72px;height:44px;background:var(--yellow);border-radius:22px}
/* clients */
.clients{position:absolute;left:122px;top:4010px;width:958px;height:70px;display:flex;align-items:center}
.client{flex:1;display:flex;align-items:center;justify-content:center;gap:10px;font-size:20px;font-weight:700;color:#2c3e6b;height:70px;border-right:1px solid #bbb;white-space:nowrap}
.client:last-child{border-right:none}
.client i{width:18px;height:18px;background:#2c3e6b;display:block}
/* footer */
.footer{position:absolute;left:0;top:4134px;width:1200px;height:435px;background:linear-gradient(180deg,#151515,#070707)}
.f-head{position:absolute;color:var(--white);font-size:18px;font-weight:700}
.f-text{position:absolute;color:#d5d5d5;font-size:14px;line-height:19px}
.f-links{position:absolute;left:518px;top:4343px;list-style:none;color:#e0e0e0;font-size:13px;line-height:17px}
.vline{position:absolute;top:4180px;width:2px;height:62px;background:var(--white)}
.social{position:absolute;top:4517px;width:28px;height:28px;border-radius:50%;border:2px solid #ddd}
</style>
</head>
<body>

<header class="nav">
  <div class="logo">Your Logo</div>
  <ul>
    <li class="active">HOME</li><li>ABOUT</li><li>SERVICES</li><li>PROJECTS</li><li>TESTIMONIALS</li><li>BLOGS</li><li>CONTACT</li>
  </ul>
  <div class="quote">GET A QUOTE</div>
</header>

<section class="hero">
  <div class="photo" role="img" aria-label="House under construction with timber framing and a crane" style="left:0;top:76px;width:1200px;height:554px;background:linear-gradient(180deg,#5d6b6f 0%,#6e6a5c 40%,#3c4a3a 75%,#2a2f28 100%)"></div>
  <div class="abs" style="left:0;top:76px;width:1200px;height:554px;background:rgba(0,0,0,.35)"></div>
  <div class="hero-text" style="top:310px;font-size:36px;font-weight:700;color:var(--yellow);letter-spacing:1px">WE INNOVATE</div>
  <div class="hero-text" style="top:368px;font-size:14px;color:var(--white)">Lorem Ipsum is simply dummy text of the printing and typesetting industry.</div>
  <div class="btn" style="left:535px;top:414px">Read More</div>
</section>

<section class="stats">
  <div class="photo" role="img" aria-label="Faint world map" style="left:230px;top:10px;width:220px;height:118px;background:radial-gradient(ellipse at center,#3a3a3a 0%,#1a1a1a 70%,#111 100%)"></div>
  <div class="abs" style="left:278px;top:45px;font-size:42px;font-weight:700;color:var(--yellow)">4,590</div>
  <div class="abs" style="left:508px;top:44px;font-size:20px;color:var(--white);letter-spacing:1px">COMPLETE <b>PROJECTS</b></div>
  <div class="abs" style="left:508px;top:76px;font-size:14px;color:#ddd">Lorem Ipsum is simply dummy text of the printing and typesetting industry.</div>
</section>

<h2 class="section-title" style="top:810px">OUR <b>SERVICES</b></h2>
<div class="photo" role="img" aria-label="Smiling builder in a yellow hard hat with crossed arms" style="left:116px;top:883px;width:250px;height:366px;background:linear-gradient(180deg,#f3c21a 0%,#e0b49a 22%,#2f3560 45%,#1f2440 100%);border-radius:40px 40px 0 0"></div>
<div class="spec-title">We Specialize In</div>
<div class="spec-copy">Lorem Ipsum is simply dummy text of the printing and typesetting industry.</div>
<div class="service" style="left:581px;color:var(--yellow)">
  <svg width="42" height="42" viewBox="0 0 42 42" fill="none" stroke="#f9c20f" stroke-width="2.5"><path d="M4 18 21 5l17 13"/><path d="M9 15v22h24V15"/><path d="M9 26h24M16 26v11M26 26v11"/></svg>
  custom deck design and builds
</div>
<div class="service" style="left:773px">
  <svg width="42" height="42" viewBox="0 0 42 42" fill="none" stroke="#111" stroke-width="2.5"><path d="M4 20 21 6l17 14"/><path d="M9 24 21 14l12 10"/><path d="M12 28h18v9H12z"/></svg>
  Custom home builds
</div>
<div class="service" style="left:935px">
  <svg width="42" height="42" viewBox="0 0 42 42" fill="none" stroke="#111" stroke-width="2.5"><path d="M10 10h18v10H10z"/><path d="M28 15h8"/><path d="M16 20l-4 16h8l2-16"/></svg>
  Commercial concrete
</div>
<div class="rule" style="top:1249px"></div>

<h2 class="section-title" style="top:1313px">OUR <b>PROECTS</b></h2>
<div class="arrows" style="left:1023px;top:1330px">
  <svg width="26" height="26" viewBox="0 0 26 26"><rect width="26" height="26" fill="#111"/><path d="M16 7 9 13l7 6z" fill="#fff"/></svg>
  <svg width="26" height="26" viewBox="0 0 26 26"><rect width="26" height="26" fill="#f9c20f"/><path d="M10 7l7 6-7 6z" fill="#111"/></svg>
</div>
<div class="photo" role="img" aria-label="Modern office building" style="left:0;top:1435px;width:300px;height:243px;background:linear-gradient(160deg,#c9d6e0,#7d8b96 60%,#4b5660)"></div>
<div class="photo" role="img" aria-label="City skyscrapers against a blue sky" style="left:300px;top:1435px;width:300px;height:243px;background:linear-gradient(180deg,#1f5fa8,#6f93bd 55%,#8c8f8e)"></div>
<div class="photo" role="img" aria-label="Commercial glass building" style="left:600px;top:1435px;width:300px;height:243px;background:linear-gradient(180deg,#b8c6d2,#8796a2)"></div>
<div class="proj-hover">
  <div class="abs" style="left:22px;top:22px;font-size:26px;color:var(--black)">Company Name</div>
  <div class="abs" style="left:22px;top:56px;font-size:16px;color:var(--black)">Location</div>
  <svg class="abs" style="left:128px;top:102px" width="44" height="44" viewBox="0 0 44 44" fill="none" stroke="#111" stroke-width="3"><circle cx="18" cy="18" r="13"/><path d="M28 28l12 12M18 12v12M12 18h12"/></svg>
</div>
<div class="photo" role="img" aria-label="Family home with brick front" style="left:900px;top:1435px;width:300px;height:243px;background:linear-gradient(180deg,#8fb4d8,#a99a86 55%,#5d7a3e)"></div>
<div class="btn" style="left:535px;top:1729px">View More</div>
<div class="rule" style="top:1812px"></div>

<h2 class="section-title" style="top:1885px;left:122px;width:auto;text-align:left">ABOUT <b>US</b></h2>
<p class="about-copy">Lorem Ipsum is simply dummy text of the printing and typesetting industry. Lorem Ipsum has been the industry's standard dummy text ever since the 1500s, when an unknown printer took a galley of type and scrambled it to make a type specimen book.</p>
<div class="photo" role="img" aria-label="Video of a concrete building site from above" style="left:634px;top:1873px;width:441px;height:244px;border:4px solid var(--yellow);background:linear-gradient(135deg,#6a6a66,#3e3e3b 60%,#8a8884)"></div>
<svg class="abs" style="left:819px;top:1960px" width="70" height="70" viewBox="0 0 70 70"><circle cx="35" cy="35" r="32" fill="rgba(255,255,255,.2)" stroke="#fff" stroke-width="3"/><path d="M28 22l20 13-20 13z" fill="#fff"/></svg>
<div class="rule" style="top:2175px"></div>

<h2 class="section-title" style="top:2233px">Teti<b class="plain">monials</b></h2>
<div class="arrows" style="left:1023px;top:2250px">
  <svg width="26" height="26" viewBox="0 0 26 26"><rect width="26" height="26" fill="#111"/><path d="M16 7 9 13l7 6z" fill="#fff"/></svg>
  <svg width="26" height="26" viewBox="0 0 26 26"><rect width="26" height="26" fill="#f9c20f"/><path d="M10 7l7 6-7 6z" fill="#111"/></svg>
</div>
<div class="t-card" style="left:122px;top:2415px;width:298px;height:220px;padding-top:62px">
  <div class="mark">&ldquo;</div>
  <div class="name">Daniel Reed</div><div class="role">Client</div><div class="stars">★★★★★</div>
  <p>Lorem Ipsum is simply dummy text of the printing and typesetting industry.</p>
  <div class="more">Read More... »</div>
</div>
<div class="avatar" role="img" aria-label="Client portrait" style="left:219px;top:2350px;width:104px;height:104px"></div>
<div class="t-card featured" style="left:439px;top:2382px;width:323px;height:262px;padding-top:108px">
  <div class="mark">&ldquo;</div>
  <div class="name">James Carter</div><div class="role">Client</div><div class="stars">★★★★★</div>
  <p>Lorem Ipsum is simply dummy text of the printing and typesetting industry.</p>
  <div class="more">Read More... »</div>
</div>
<div class="avatar" role="img" aria-label="Client portrait" style="left:530px;top:2337px;width:140px;height:140px;border-color:var(--black)"></div>
<div class="t-card" style="left:783px;top:2415px;width:298px;height:220px;padding-top:62px">
  <div class="mark">&ldquo;</div>
  <div class="name">Morgan Lee</div><div class="role">Client</div><div class="stars">★★★★★</div>
  <p>Lorem Ipsum is simply dummy text of the printing and typesetting industry.</p>
  <div class="more">Read More... »</div>
</div>
<div class="avatar" role="img" aria-label="Client portrait" style="left:880px;top:2350px;width:104px;height:104px"></div>
<div class="dots" style="left:560px;top:2680px"><span></span><span class="on"></span><span></span></div>
<div class="btn" style="left:535px;top:2725px">View More</div>
<div class="rule" style="top:2796px"></div>

<h2 class="section-title" style="top:2852px">OUR LATEST <b>BLOGS</b></h2>
<div class="arrows" style="left:1023px;top:2870px">
  <svg width="26" height="26" viewBox="0 0 26 26"><rect width="26" height="26" fill="#111"/><path d="M16 7 9 13l7 6z" fill="#fff"/></svg>
  <svg width="26" height="26" viewBox="0 0 26 26"><rect width="26" height="26" fill="#f9c20f"/><path d="M10 7l7 6-7 6z" fill="#111"/></svg>
</div>
<article class="blog" style="left:125px;width:301px">
  <div class="img" role="img" aria-label="Tower crane over a building under construction" style="background:linear-gradient(180deg,#4f88c6,#8fb2d6 50%,#8a5a3a)"></div>
  <div class="date"><b>21</b>March 2018</div>
  <h3>TITLE 1</h3>
  <p>Lorem Ipsum is simply dummy text of the printing and typesetting industry.</p>
  <div class="meta"><span>Read More...</span><span>♡ 28 &nbsp; ◌ 28</span></div>
</article>
<article class="blog featured" style="left:454px;width:298px">
  <div class="img" role="img" aria-label="Timber-framed house under construction" style="background:linear-gradient(180deg,#7aa8d4,#a08a70 55%,#5e4a36)"></div>
  <div class="date"><b>22</b>March 2018</div>
  <h3>TITLE 2</h3>
  <p>Lorem Ipsum is simply dummy text of the printing and typesetting industry.</p>
  <div class="meta"><span>Read More...</span><span>♡ 28 &nbsp; ◌ 28</span></div>
</article>
<article class="blog" style="left:780px;width:298px">
  <div class="img" role="img" aria-label="Colourful apartment blocks" style="background:linear-gradient(180deg,#5d9ad6,#d0a874 55%,#b8b3a8)"></div>
  <div class="date"><b>23</b>March 2018</div>
  <h3>TITLE 3</h3>
  <p>Lorem Ipsum is simply dummy text of the printing and typesetting industry.</p>
  <div class="meta"><span>Read More...</span><span>♡ 28 &nbsp; ◌ 28</span></div>
</article>
<div class="dots" style="left:560px;top:3426px"><span></span><span class="on"></span><span></span></div>
<div class="btn" style="left:535px;top:3470px">View More</div>
<div class="rule" style="top:3549px"></div>

<h2 class="section-title" style="top:3600px"><b style="padding:14px 12px 6px 4px">SUBSCRIBE</b></h2>
<div class="abs" style="left:0;top:3680px;width:1200px;text-align:center;font-size:12px;color:var(--black);letter-spacing:.5px">SUBSCRIBE TO OUR NEWSLETTER</div>
<div class="subscribe-box"><span>YOUR E-MAIL HERE</span><i></i></div>
<svg class="abs" style="left:792px;top:3735px" width="24" height="22" viewBox="0 0 24 22"><path d="M1 10 23 1 17 21l-6-7z" fill="#fff"/></svg>
<div class="rule" style="top:3832px"></div>

<h2 class="section-title" style="top:3893px">OUR <b>CLIENTS</b></h2>
<div class="clients">
  <div class="client"><i></i>Harlow Builders</div>
  <div class="client"><i></i>Pinecrest</div>
  <div class="client"><i></i>Stonefield</div>
  <div class="client"><i></i>Meridian Build</div>
  <div class="client" style="color:#8a1c1c">Corbett Co.</div>
</div>

<footer class="footer"></footer>
<div class="f-head" style="left:122px;top:4180px">Call Us Now</div>
<div class="f-text" style="left:122px;top:4208px">202 555 0147</div>
<div class="vline" style="left:385px"></div>
<div class="f-head" style="left:518px;top:4180px">Come Visit Now</div>
<div class="f-text" style="left:518px;top:4208px">48 Cedar Lane, Harbor City,<br>FL 32000</div>
<div class="vline" style="left:815px"></div>
<div class="f-head" style="left:923px;top:4180px">Send Massage</div>
<div class="f-text" style="left:923px;top:4208px">info@examplebuild.com</div>
<div class="abs" style="left:122px;top:4298px;font-size:30px;font-weight:700;color:var(--yellow)">YOUR LOGO</div>
<div class="f-text" style="left:122px;top:4345px;width:200px">Lorem Ipsum is simply dummy text of the printing and typesetting industry.</div>
<div class="f-text" style="left:122px;top:4440px;font-size:12px">Read More »</div>
<div class="f-head" style="left:518px;top:4300px;font-size:24px">Quick Link</div>
<ul class="f-links"><li>HOME</li><li>ABOUT US</li><li>SERVICES</li><li>PROJECTS</li><li>TESTIMONIALS</li><li>BLOGS</li><li>CONTACT US</li></ul>
<div class="f-head" style="left:786px;top:4300px;font-size:24px">Subscribe Now</div>
<div class="abs" style="left:786px;top:4362px;width:294px;height:30px;border:1px solid #ccc"></div>
<div class="f-text" style="left:796px;top:4368px;font-size:12px">E-Mail</div>
<svg class="abs" style="left:1040px;top:4368px" width="20" height="18" viewBox="0 0 24 22"><path d="M1 10 23 1 17 21l-6-7z" fill="#fff"/></svg>
<div class="abs" style="left:122px;top:4500px;width:958px;height:1px;background:#666"></div>
<div class="f-text" style="left:122px;top:4522px;font-size:13px">CopyRight © 2018 company name. All Right Reserve</div>
<div class="social" style="left:1012px"></div>
<div class="social" style="left:1046px"></div>
<div class="social" style="left:1080px"></div>

</body>
</html>
```